Government Contracts One Page Marketing Piece

Create a one page flyer. Will need one graphic design created the rest is just layout with the following text

HEADLINE: Introducing Your Newest Customer.

GRAPHIC: (PICTURE OF THE STATE OF IL OR USA WITH IL POPPING OUT.)

UNDER GRAPHIC, SUBHEAD: Thousands of government contracts are awarded to businesses every year. Let's make sure your business is one of them. 

BODY COPY: At 2727, we help you tap into the tremendous amount of government contract work needed for 6,963 units of local government in Illinois. Combining legal, PR, marketing, and lobbying expertise in one stop, we’re ready to be your advocate and connect your business with government.

(SIX BLUE BOXES)

Business Development
2727 keeps a watchful eye out for government opportunities that match up with your business. We do whatever it takes to help you win those contracts. Plus, we have relationships with businesses, unions and nonprofits across the state. We’ll help you win those contracts, too.

Government Marketing
2727 helps you market yourself to government agencies. We refine your message and RFP responses to help you stand out and land the deal.

Procurement Hassles
2727 helps you navigate the procurement process. Procedural errors on RFP, RFI, or RFQ responses can obliterate your chances of winning. We handle the bureaucratic requirements so you can focus on running your business.

Government Relations And Lobbying
2727 is your advocate. Want to change the law or stop a bad piece of legislation? We’ll work with you and policymakers to ensure you are well represented. We also assist in situations where you need government to either help your business or get out of the way.

Strategic Communication
2727 launches PR plans that support your key objectives. Our words and phrases get results, in business and government. We get your message to the right people at the right time. 

Grassroots & Coalition Development
2727 utilizes our experience and relationships to build the largest possible network of supporters to enhance your legislative goals. We build coalitions that bring credibility and emphasize broad-base support.

LOGO, CONTACT

Target Market(s)

businesses that want to grow

Font styles to use
Other font styles liked:
• Trajan Bold

Requirements
Must have
• Image should be of US Map with cities but with a pop out of Illinois with all the cities marked. Would love some cool design for this, would prefer it be one or two colors but not tons. See attached photos that would need to be merged and made to look nice. Illinois would need to be somewhat larger on the pop-out USA image.
• Can you try to variations with different style maps
• Fun style
• http://www.pixelvaultimages.example/pic-455215429/stock-vector-usa-map-word-cloud-collage-with-most-important-cities.html?src=undefined-undefined-21
• and
• http://www.pixelvaultimages.example/pic-103082810/stock-photo-word-cloud-map-of-illinois-state-usa.html?src=PxorPAIOyuLnwqL7O5J1hg-1-7
• Simple style
• http://www.pixelvaultimages.example/pic-251329126/stock-vector-illinois-map.html?src=-P5kt_NviDiYq8QyexsQog-1-6
• and
• http://www.pixelvaultimages.example/pic-34919179/stock-vector-map-of-usa-vector.html?src=ftt8pniMj4Ck2t31iIo1tQ-1-39
Nice to have
• look and feel like my website www.2727counselgroup.example
• font used for logo was Trajan Bold

```html
<!DOCTYPE html>
<html lang="en">
<head>
<meta charset="utf-8">
<title>2727 Counsel Group – Government Contracts</title>
<link rel="stylesheet" href="https://fonts.googleapis.com/css2?family=Arimo:wght@400;700&family=Cinzel:wght@700&display=swap">
<style>
  :root {
    --navy: #243a73;
    --navy-dark: #17285a;
    --panel-grey: #e6e7e8;
    --stripe-grey: #b9babc;
    --band-grey: #8c8d8f;
    --footer-grey: #b3b4b6;
    --ink: #2b2b2b;
    --white: #ffffff;
    --map-warm: #d9a441;
    --map-cool: #3f7cc0;
  }
  * { box-sizing: border-box; margin: 0; padding: 0; }
  html, body {
    width: 1031px; height: 1200px; overflow: hidden;
    background: var(--white);
    font-family: "Arimo", Arial, sans-serif;
  }
  .flyer { position: relative; width: 1031px; height: 1200px; background: var(--panel-grey); }

  /* Top hero */
  .hero { position: absolute; left: 0; top: 0; width: 1031px; height: 485px; }
  .hero-bg { position: absolute; inset: 0; }
  .brand {
    position: absolute; left: 42px; top: 36px;
    display: flex; align-items: center; gap: 14px;
  }
  .brand-square { width: 86px; height: 86px; background: var(--navy); }
  .brand-name {
    font-family: "Cinzel", "Times New Roman", serif; font-weight: 700;
    font-size: 30px; line-height: 1.1; color: var(--navy); letter-spacing: 1px;
  }
  .headline {
    position: absolute; left: 38px; top: 178px;
    font-size: 42px; line-height: 1.14; font-weight: 400;
    color: var(--navy); text-transform: uppercase;
  }
  .subhead {
    position: absolute; left: 22px; top: 372px; width: 600px;
    font-size: 19px; line-height: 1.3; color: var(--white);
  }
  .map-art { position: absolute; left: 642px; top: 18px; width: 380px; height: 462px; }

  /* Intro band */
  .intro {
    position: absolute; left: 0; top: 485px; width: 1031px; height: 130px;
    background: var(--band-grey); color: var(--white);
    padding: 24px 22px 0 22px;
    font-size: 19.5px; line-height: 1.36;
  }

  /* Services */
  .services {
    position: absolute; left: 6px; top: 635px; width: 1019px;
    display: grid; grid-template-columns: 310px 320px 332px; column-gap: 14px;
    grid-template-rows: 232px 235px; row-gap: 10px;
  }
  .service { background: var(--navy); color: var(--white); padding: 18px 20px 0 20px; }
  .service-title { font-size: 16.5px; font-weight: 400; text-transform: uppercase; line-height: 1.15; margin-bottom: 4px; }
  .service p { font-size: 16.5px; line-height: 1.2; text-align: justify; }
  .service p + p { margin-top: 19px; }

  /* Footer */
  .footer { position: absolute; left: 0; top: 1136px; width: 1031px; height: 64px; }
  .footer-bg { position: absolute; inset: 0; }
  .footer-url {
    position: absolute; left: 92px; top: 18px;
    color: var(--white); font-size: 22px; letter-spacing: 2px;
  }
  .footer-icon { position: absolute; left: 42px; top: 17px; }
  .footer-contact {
    position: absolute; right: 22px; top: 27px;
    color: var(--ink); font-size: 17px;
  }
</style>
</head>
<body>
<main class="flyer">
  <section class="hero">
    <svg class="hero-bg" width="1031" height="485" viewBox="0 0 1031 485">
      <rect x="0" y="0" width="1031" height="485" fill="var(--white)"/>
      <polygon points="0,0 384,0 598,485 0,485" fill="var(--panel-grey)"/>
      <polygon points="384,0 444,0 662,485 598,485" fill="var(--stripe-grey)"/>
      <polygon points="0,364 662,364 640,430 0,430" fill="var(--navy)"/>
      <polygon points="600,430 640,430 662,458" fill="var(--navy-dark)"/>
    </svg>

    <div class="brand">
      <div class="brand-square"></div>
      <div class="brand-name">2727 COUNSEL<br>GROUP</div>
    </div>

    <h1 class="headline">Introducing<br>your newest<br>customer.</h1>

    <p class="subhead">Thousands of government contracts are awarded to businesses every year. Let's make sure your business is one of them.</p>

    <svg class="map-art" role="img" aria-label="Word-cloud map of Illinois made of city names in many colours" viewBox="0 0 380 462">
      <defs>
        <linearGradient id="mapTone" x1="0" y1="0" x2="1" y2="1">
          <stop offset="0" stop-color="var(--map-cool)" stop-opacity="0.35"/>
          <stop offset="1" stop-color="var(--map-warm)" stop-opacity="0.35"/>
        </linearGradient>
      </defs>
      <rect width="380" height="462" fill="url(#mapTone)"/>
    </svg>
  </section>

  <p class="intro">At 2727, we help you tap into the tremendous amount of government contract work needed for 6,963 units of local government in Illinois. Combining legal, PR, marketing, and lobbying expertise in one stop, we’re ready to be your advocate and connect your business with government.</p>

  <section class="services">
    <article class="service">
      <h2 class="service-title">Business Development</h2>
      <p>2727 keeps a watchful eye out for government opportunities that match up with your business. We do whatever it takes to help you win those contracts. Plus, we have relationships with businesses, unions and nonprofits across the state. We’ll help you win those contracts, too.</p>
    </article>
    <article class="service">
      <h2 class="service-title">Government Marketing</h2>
      <p>2727 helps you market yourself to government agencies.</p>
      <p>We refine your message and RFP responses to help you stand out and land the deal.</p>
    </article>
    <article class="service">
      <h2 class="service-title">Procurement Hassles</h2>
      <p>2727 helps you navigate the procurement process. Procedural errors on RFP, RFI, or RFQ responses can obliterate your chances of winning. We handle the bureaucratic requirements so you can focus on running your business.</p>
    </article>
    <article class="service">
      <h2 class="service-title">Government Relations<br>and Lobbying</h2>
      <p>2727 is your advocate. Want to change the law or stop a bad piece of legislation? We’ll work with you and policymakers to ensure you are well represented. We also assist in situations where you need government to either help your business or get out of the way.</p>
    </article>
    <article class="service">
      <h2 class="service-title">Strategic Communication</h2>
      <p>2727 launches PR plans that support your key objectives. Our words and phrases get results, in business and government.</p>
      <p>We get your message to the right people at the right time.</p>
    </article>
    <article class="service">
      <h2 class="service-title">Grassroots &amp; Coalition<br>Development</h2>
      <p>2727 utilizes our experience and relationships to build the largest possible network of supporters to enhance your legislative goals. We build coalitions that bring credibility and emphasize broad-base support.</p>
    </article>
  </section>

  <footer class="footer">
    <svg class="footer-bg" width="1031" height="64" viewBox="0 0 1031 64">
      <rect width="1031" height="64" fill="var(--panel-grey)"/>
      <polygon points="470,16 1031,16 1031,64 490,64" fill="var(--footer-grey)"/>
      <polygon points="0,0 452,0 490,64 0,64" fill="var(--navy)"/>
    </svg>
    <svg class="footer-icon" width="30" height="30" viewBox="0 0 30 30" aria-hidden="true">
      <g fill="none" stroke="var(--white)" stroke-width="2">
        <circle cx="15" cy="15" r="13"/>
        <ellipse cx="15" cy="15" rx="6" ry="13"/>
        <line x1="2" y1="15" x2="28" y2="15"/>
        <line x1="4.5" y1="8" x2="25.5" y2="8"/>
        <line x1="4.5" y1="22" x2="25.5" y2="22"/>
      </g>
    </svg>
    <span class="footer-url">www.2727counselgroup.example</span>
    <span class="footer-contact">Dana Whitfield at 555-014-2730 for more information</span>
  </footer>
</main>
</body>
</html>
```